Brochure update and matching sign-up form

We are a high end Tanning Salon that offers multiple levels of Tanning, Red Light, Sunless, and Hybrid (UV and Red Light in a single session).

I want to modernize our current brochure (the original is included in the links below, along with some changes to it), and add a sign-up form for new clients that helps guide them through the purchasing process.

I want the sign-up form to be 11 x 17 double sided, with the demographics and purchasing information on one side, and the waiver/terms on the back side. This form needs to be super clean and easy to fill out, and should lead the client through the sign-up and purchasing options. Without knowing how this might look or how much space it will take, I do anticipate revisions after the first draft.

The information provided in the links isn't formatted as good as I would normally like, but you'll obviously keep the layout consistent. There will be some images needed after the first draft.

Once done, I will probably need these in various formats (print and digital) with any necessary revisions to accommodate the various formats and uses.

See links:

Brochure Revisions: https://www.plumaleaf.net/vault/k72/pg/a3d9e104-c6f1-527b-b914-7a20c5d88e61/QxRmTobN4H2vKf8Y63wzrpLdSjT5EkoMU_7hGyBwXcDqNaVzPtfu-3o8Rm

Sign-up form: https://www.plumaleaf.net/vault/k72/pg/2e7b90d3-5a4c-6f1e-839a-c04d6a71be95/hTzQpLwy3N6GdRvAj1xKsbMeUc9Fo47YXiEtD529HWnZkCrBp8Jv4Q7uxL

```html
<!DOCTYPE html>
<html lang="en">
<head>
<meta charset="utf-8">
<title>SunHaven Tanning Brochure</title>
<link href="https://fonts.googleapis.com/css2?family=Poppins:wght@400;500;600;700;800&family=Arimo:wght@400&display=swap" rel="stylesheet">
<style>
:root{
  --navy:#124676;
  --navy-deep:#0f3f6c;
  --yellow:#fdd041;
  --gold:#fcc93a;
  --ink:#1f2b38;
  --grey:#6b7380;
  --frame:#9a9a9a;
  --white:#ffffff;
}
*{margin:0;padding:0;box-sizing:border-box}
html,body{width:1200px;height:1000px;overflow:hidden;background:var(--white)}
body{font-family:"Poppins",sans-serif;color:var(--ink)}
.sheet{position:absolute;left:0;top:0;width:2100px;height:1750px;transform:scale(0.5714286);transform-origin:0 0}
.abs{position:absolute}
.frame{left:40px;top:222px;width:2020px;height:1305px;border:2px solid var(--frame)}

/* left page */
.big-five{left:104px;top:236px;font-size:118px;font-weight:800;color:var(--yellow);line-height:1}
.title-band{left:168px;top:268px;width:892px;height:75px;background:var(--navy);color:var(--white);font-size:31px;font-weight:700;padding-left:25px;line-height:75px}
.col-head{font-size:10.5px;text-align:center;line-height:1.1;color:var(--ink);transform:translateX(-50%);white-space:nowrap}
.equip-head{left:153px;top:386px;font-size:17px}
.head-rule{left:55px;top:418px;width:1005px;height:10px;background:var(--navy)}
.row-rule{height:2px;background:var(--navy)}
.row-num{font-size:36px;font-weight:700;color:var(--navy);line-height:1}
.img-slot{width:74px;height:48px;border:1.5px solid #8a8a8a;font-size:7.5px;line-height:10px;text-align:center;padding-top:8px;color:#555;background:var(--white)}
.unit-name{font-size:13px;font-weight:700;color:var(--ink);line-height:1.05}
.unit-desc{font-size:10.3px;line-height:11.5px;color:var(--ink)}
.price{font-size:23px;font-weight:700;color:var(--navy);line-height:28px;white-space:nowrap}
.price small{font-size:12px;font-weight:600}
.price .per{font-size:12px;font-weight:600}
.single{transform:translateX(-50%)}
.stack{transform:translateX(-50%);display:flex;flex-direction:column;align-items:center}
.stack .or{font-size:11px;line-height:24px}
.stack .note{font-size:11px;font-weight:600;line-height:16px}
.visual{border-radius:4px}
.footnote{font-family:"Arimo",sans-serif;font-size:11px;line-height:13px;color:var(--grey)}

/* right page */
.panel{left:1061px;top:225px;width:996px;height:897px;background:var(--navy)}
.panel-text{color:var(--white)}
.h-big{font-size:32px;font-weight:700;line-height:1}
.h-big .accent{color:var(--gold)}
.lead{font-size:19px;line-height:22px}
.plan-name{font-size:28px;font-weight:500;color:var(--white);transform:translateX(-50%);white-space:nowrap}
.plan-name b{font-weight:700}
.plan-price{transform:translateX(-50%);white-space:nowrap;color:var(--white);font-size:31px;font-weight:500;line-height:1}
.plan-price span{font-size:56px;font-weight:700;color:var(--gold)}
.perks{left:1133px;top:637px;list-style:none;color:var(--white);font-size:19px;line-height:32.5px}
.perks li{display:flex;align-items:flex-start;gap:9px}
.perks svg{margin-top:10px;flex:none}
.perks .fine{display:block;font-size:16px;line-height:14px}
.offer-box{background:var(--white);border-radius:8px}
.tab{transform:translateX(-50%);background:var(--yellow);color:var(--navy);font-size:21px;font-weight:700;border-radius:16px;padding:0 16px;line-height:31px;white-space:nowrap}
.box-sub{transform:translateX(-50%);font-size:20px;font-weight:600;color:var(--ink);white-space:nowrap}
.upgrade{width:128px;height:123px;background:var(--navy);border-radius:10px;overflow:hidden;text-align:center;color:var(--white)}
.upgrade .get{margin-top:10px;font-size:19px;font-weight:700;color:var(--gold);line-height:22px}
.upgrade .in{font-size:13.5px;line-height:17px}
.upgrade .for{font-size:19px;font-weight:700;color:var(--gold);line-height:24px}
.upgrade .for small{font-size:13px;font-weight:500;color:var(--white)}
.saving{position:absolute;left:31px;top:84px;width:66px;height:66px;border-radius:50%;background:var(--white);color:var(--navy);padding-top:3px}
.saving b{display:block;font-size:19px;line-height:19px;font-weight:700}
.saving span{display:block;font-size:12.5px;line-height:14px}
.gift{width:200px;height:42px;background:var(--navy);color:var(--white);font-size:13.5px;line-height:42px;padding-left:11px;border-radius:2px}
.gift em{font-style:normal;color:var(--gold)}
.gift-note{transform:translateX(-50%);font-size:13.5px;color:var(--ink);white-space:nowrap}
.rec-band{left:1061px;top:1153px;width:996px;height:43px;background:var(--yellow);color:var(--white);font-size:31px;font-weight:700;text-align:center;line-height:43px}
.rec-title{font-size:21px;font-weight:500;color:var(--navy);line-height:24px}
.rec-copy{font-size:12.6px;line-height:13px;color:var(--ink)}
</style>
</head>
<body>
<div class="sheet">
  <div class="abs frame"></div>

  <!-- Pricing page -->
  <div class="abs big-five">5</div>
  <div class="abs title-band">Levels of UV Tanning, Sunless, Hybrid &amp; Red Light</div>

  <div class="abs equip-head">Equipment</div>
  <div class="abs col-head" style="left:461px;top:370px">Best&nbsp; Monthly<br>Rate When<br>Paid Annually</div>
  <div class="abs col-head" style="left:557px;top:381px">Monthy Auto-Pay<br>Commitment</div>
  <div class="abs col-head" style="left:641px;top:370px">Monthy<br>Auto-Pay<br>Flex</div>
  <div class="abs col-head" style="left:706px;top:381px">30 Day<br>Unlimited</div>
  <div class="abs col-head" style="left:774px;top:393px">Single Visit</div>
  <div class="abs col-head" style="left:863px;top:371px">Buy 5, Get 2<br>Free Sessions<br>Valid for 365 days</div>
  <div class="abs col-head" style="left:972px;top:371px">Buy 10, Get 5<br>Free Sessions<br>Valid for 365 days</div>
  <div class="abs head-rule"></div>

  <!-- Level 1 -->
  <div class="abs row-num" style="left:108px;top:447px">1</div>
  <div class="abs img-slot" style="left:140px;top:450px">PRODUCT<br>IMAGE<br>HERE</div>
  <div class="abs unit-name" style="left:140px;top:507px">Sunbreeze</div>
  <div class="abs unit-desc" style="left:140px;top:527px;width:230px">Lorem ipsum dolor sit amet, consectetuer adipiscing elit, sed</div>
  <div class="abs stack" style="left:459px;top:455px">
    <div class="price">$29<span class="per">/Month</span></div><div class="or">Or</div><div class="price">$345</div><div class="note">Annually</div>
  </div>
  <div class="abs price single" style="left:557px;top:484px">$33<small>.88</small></div>
  <div class="abs price single" style="left:637px;top:482px">$37<small>.88</small></div>
  <div class="abs price single" style="left:706px;top:482px">$75</div>
  <div class="abs price single" style="left:773px;top:482px">$13</div>
  <div class="abs price single" style="left:863px;top:486px">$65</div>
  <div class="abs stack" style="left:972px;top:452px">
    <div class="price">$130</div><div class="or">Or</div><div class="price">$8<small>.66</small></div><div class="note">Each</div>
  </div>
  <div class="abs row-rule" style="left:62px;top:561px;width:998px"></div>

  <!-- Levels 2 & 3 -->
  <div class="abs row-num" style="left:108px;top:580px">2</div>
  <div class="abs img-slot" style="left:140px;top:583px">PRODUCT<br>IMAGE<br>HERE</div>
  <div class="abs unit-name" style="left:140px;top:640px">Klasse</div>
  <div class="abs unit-desc" style="left:140px;top:661px;width:230px">Lorem ipsum dolor sit amet, consectetuer adipiscing elit, sed</div>
  <div class="abs row-num" style="left:108px;top:703px">3</div>
  <div class="abs img-slot" style="left:140px;top:705px">PRODUCT<br>IMAGE<br>HERE</div>
  <div class="abs img-slot" style="left:226px;top:705px">PRODUCT<br>IMAGE<br>HERE</div>
  <div class="abs img-slot" style="left:311px;top:705px">PRODUCT<br>IMAGE<br>HERE</div>
  <div class="abs unit-name" style="left:140px;top:762px">Aspire</div>
  <div class="abs unit-name" style="left:226px;top:762px">Classic Legs</div>
  <div class="abs unit-name" style="left:311px;top:762px">Super Vortex<br>Stand-Up</div>
  <div class="abs unit-desc" style="left:140px;top:797px;width:330px">Lorem ipsum dolor sit amet, consectetuer adipiscing elit, sed diam nonummy nibh euismod tincidunt ut laoreet dolore magna aliquam erat volutpat. Ut wisi enim ad minim veniam, quis nostrud exerci tation ullamcorper suscipit lobortis nisl ut aliquip ex ea</div>
  <div class="abs stack" style="left:459px;top:659px">
    <div class="price">$39<span class="per">/Month</span></div><div class="or">Or</div><div class="price">$465</div><div class="note">Annually</div>
  </div>
  <div class="abs price single" style="left:557px;top:688px">$45<small>.88</small></div>
  <div class="abs price single" style="left:637px;top:686px">$58<small>.88</small></div>
  <div class="abs price single" style="left:706px;top:686px">$95</div>
  <div class="abs price single" style="left:773px;top:686px">$18</div>
  <div class="abs price single" style="left:863px;top:690px">$90</div>
  <div class="abs stack" style="left:972px;top:656px">
    <div class="price">$180</div><div class="or">Or</div><div class="price">$12<small>.66</small></div><div class="note">Each</div>
  </div>
  <div class="abs row-rule" style="left:62px;top:861px;width:998px"></div>

  <!-- Level 4 -->
  <div class="abs row-num" style="left:108px;top:880px">4</div>
  <div class="abs img-slot" style="left:140px;top:884px">PRODUCT<br>IMAGE<br>HERE</div>
  <div class="abs img-slot" style="left:226px;top:884px">PRODUCT<br>IMAGE<br>HERE</div>
  <div class="abs unit-name" style="left:140px;top:942px">Apex 250</div>
  <div class="abs unit-desc" style="left:140px;top:962px;width:282px">Lorem ipsum dolor sit amet, consectetuer adipiscing elit, sed diam nonummy nibh euismod tincidunt ut laoreet dolore magna aliquam erat volutpat. Ut wisi enim ad minim veniam, quis</div>
  <div class="abs stack" style="left:459px;top:895px">
    <div class="price">$49<span class="per">/Month</span></div><div class="or">Or</div><div class="price">$588</div><div class="note">Annually</div>
  </div>
  <div class="abs price single" style="left:557px;top:924px">$56<small>.88</small></div>
  <div class="abs price single" style="left:637px;top:922px">$69<small>.88</small></div>
  <div class="abs price single" style="left:706px;top:922px">$125</div>
  <div class="abs price single" style="left:773px;top:922px">$22</div>
  <div class="abs price single" style="left:863px;top:926px">$110</div>
  <div class="abs stack" style="left:972px;top:892px">
    <div class="price">$220</div><div class="or">Or</div><div class="price">$14<small>.66</small></div><div class="note">Each</div>
  </div>
  <div class="abs row-rule" style="left:67px;top:1031px;width:993px"></div>

  <!-- Level 5 -->
  <div class="abs row-num" style="left:108px;top:1058px">5</div>
  <div class="abs img-slot" style="left:140px;top:1061px">PRODUCT<br>IMAGE<br>HERE</div>
  <div class="abs visual" role="img" aria-label="High pressure tanning bed product photo" style="left:258px;top:1062px;width:57px;height:43px;background:linear-gradient(160deg,#5d86c4,#2b3f7a)"></div>
  <div class="abs unit-name" style="left:140px;top:1119px">Regent</div>
  <div class="abs unit-name" style="left:258px;top:1119px">High Pressure</div>
  <div class="abs unit-desc" style="left:140px;top:1140px;width:282px">Lorem ipsum dolor sit amet, consectetuer adipiscing elit, sed diam nonummy nibh euismod tincidunt ut laoreet dolore magna aliquam erat volutpat. Ut wisi enim ad minim veniam, quis nostrud exerci tation ullamcorper suscipit lobortis</div>
  <div class="abs stack" style="left:459px;top:1076px">
    <div class="price">$66<span class="per">/Month</span></div><div class="or">Or</div><div class="price">$799</div><div class="note">Annually</div>
  </div>
  <div class="abs price single" style="left:557px;top:1105px">$76<small>.88</small></div>
  <div class="abs price single" style="left:637px;top:1103px">$94<small>.88</small></div>
  <div class="abs price single" style="left:706px;top:1103px">$149</div>
  <div class="abs price single" style="left:773px;top:1103px">$39</div>
  <div class="abs price single" style="left:863px;top:1107px">$195</div>
  <div class="abs stack" style="left:972px;top:1072px">
    <div class="price">$390</div><div class="or">Or</div><div class="price">$26<small>.66</small></div><div class="note">Each</div>
  </div>
  <div class="abs row-rule" style="left:67px;top:1222px;width:993px"></div>

  <!-- All Access -->
  <div class="abs" style="left:108px;top:1236px;font-size:22px;font-weight:700;color:var(--navy)">All Access</div>
  <div class="abs visual" role="img" aria-label="Hybrid stand-up booth product photo" style="left:143px;top:1273px;width:30px;height:45px;background:linear-gradient(180deg,#b9d3ea,#7fa6cc)"></div>
  <div class="abs visual" role="img" aria-label="Hybrid tanning bed product photo" style="left:190px;top:1275px;width:60px;height:42px;background:linear-gradient(180deg,#c9d6e4,#e8a0a6)"></div>
  <div class="abs img-slot" style="left:274px;top:1272px">PRODUCT<br>IMAGE<br>HERE</div>
  <div class="abs unit-name" style="left:140px;top:1329px">Hybrid</div>
  <div class="abs unit-name" style="left:275px;top:1329px">MistSpa Pro</div>
  <div class="abs unit-desc" style="left:140px;top:1350px;width:255px">With All-Access, enjoy the use of 5 Levels of UV tanning, all Hybrid options, Sunless, and Red Light Therapy.&nbsp; All All-Access session packages are valid towards the use of any service we offer.</div>
  <div class="abs stack" style="left:459px;top:1272px">
    <div class="price">$74<span class="per">/Month</span></div><div class="or">Or</div><div class="price">$888</div><div class="note">Annually</div>
  </div>
  <div class="abs price single" style="left:557px;top:1300px">$99<small>.88</small></div>
  <div class="abs price single" style="left:637px;top:1298px">$119<small>.88</small></div>
  <div class="abs price single" style="left:706px;top:1298px">$169</div>
  <div class="abs price single" style="left:773px;top:1298px">$39</div>
  <div class="abs price single" style="left:863px;top:1302px">$195</div>
  <div class="abs stack" style="left:972px;top:1268px">
    <div class="price">$390</div><div class="or">Or</div><div class="price">$26<small>.66</small></div><div class="note">Each</div>
  </div>
  <div class="abs row-rule" style="left:40px;top:1416px;width:995px"></div>

  <div class="abs footnote" style="left:109px;top:1433px;width:185px">Commitment – cannot cancel until 11 full monthly payments, and with 31 days notice</div>
  <div class="abs footnote" style="left:309px;top:1446px;width:245px">Flex – cancel anytime after your 1st full monthly payment, and with 31 days' notice. $35 sign-up.</div>
  <div class="abs footnote" style="left:574px;top:1433px;width:290px">Freeze any auto-pay membership for $5/month – credited back to account&nbsp; upon activation.&nbsp; Commitment membership cannot be frozen until commitment met.</div>
  <div class="abs footnote" style="left:881px;top:1445px;width:145px">Session packs valid for 1 year from date of purchase.</div>

  <!-- Membership panel -->
  <div class="abs panel"></div>
  <div class="abs panel-text h-big" style="left:1105px;top:268px">Get the <span class="accent">Freedom Membership</span></div>
  <div class="abs panel-text lead" style="left:1105px;top:310px">Freedom Plans.&nbsp; The choice for those who only tan once<br>or twice a month, but want access to discounted rates.</div>

  <svg class="abs" style="left:1150px;top:375px" width="620" height="200" viewBox="0 0 620 200" aria-hidden="true">
    <ellipse cx="133" cy="100" rx="128" ry="95" fill="none" stroke="#fdd041" stroke-width="4"/>
    <ellipse cx="477" cy="100" rx="128" ry="95" fill="none" stroke="#fdd041" stroke-width="4"/>
  </svg>
  <div class="abs plan-name" style="left:1288px;top:424px">Freedom <b>One</b></div>
  <div class="abs plan-price" style="left:1283px;top:465px"><span>$25</span>/month</div>
  <div class="abs plan-name" style="left:1632px;top:424px">Freedom <b>Two</b></div>
  <div class="abs plan-price" style="left:1627px;top:465px"><span>$29</span>/month</div>

  <div class="abs panel-text" style="left:1105px;top:598px;font-size:19px">All Freedom member's receive:</div>
  <ul class="abs perks">
    <li><svg width="15" height="15" viewBox="0 0 16 16" aria-hidden="true"><circle cx="8" cy="8" r="3.5" fill="#fcc93a"/><g stroke="#fcc93a" stroke-width="1.6" stroke-linecap="round"><path d="M8 1v2M8 13v2M1 8h2M13 8h2M3 3l1.4 1.4M11.6 11.6L13 13M3 13l1.4-1.4M11.6 4.4L13 3"/></g></svg><span>Use of their monthly sessions in ANY UV, Sunless, or Hybrid bed.</span></li>
    <li><svg width="15" height="15" viewBox="0 0 16 16" aria-hidden="true"><circle cx="8" cy="8" r="3.5" fill="#fcc93a"/><g stroke="#fcc93a" stroke-width="1.6" stroke-linecap="round"><path d="M8 1v2M8 13v2M1 8h2M13 8h2M3 3l1.4 1.4M11.6 11.6L13 13M3 13l1.4-1.4M11.6 4.4L13 3"/></g></svg><span>All additional drop-ins are just $25 for any bed.</span></li>
    <li><svg width="15" height="15" viewBox="0 0 16 16" aria-hidden="true"><circle cx="8" cy="8" r="3.5" fill="#fcc93a"/><g stroke="#fcc93a" stroke-width="1.6" stroke-linecap="round"><path d="M8 1v2M8 13v2M1 8h2M13 8h2M3 3l1.4 1.4M11.6 11.6L13 13M3 13l1.4-1.4M11.6 4.4L13 3"/></g></svg><span>Access to Freedom Buy 5, Get 5 Free<span class="fine">(no expiry on these sessions for as long as you maintain your membership).</span></span></li>
  </ul>

  <div class="abs panel-text h-big" style="left:1105px;top:765px">More Ways To <span class="accent">Save!</span></div>
  <div class="abs panel-text lead" style="left:1105px;top:807px">Freedom Plans.&nbsp; The choice for those who only tan once<br>or twice a month, but want access to discounted rates.</div>

  <!-- Upgrades box -->
  <div class="abs offer-box" style="left:1105px;top:887px;width:435px;height:195px"></div>
  <div class="abs tab" style="left:1321px;top:872px">Save on Upgrades</div>
  <div class="abs box-sub" style="left:1321px;top:907px">Ask us how!</div>
  <div class="abs upgrade" style="left:1120px;top:943px"><div class="get">Get $100</div><div class="in">In Upgrades</div><div class="for">For $80<small>Only</small></div><div class="saving"><b>20%</b><span>Savings</span></div></div>
  <div class="abs upgrade" style="left:1258px;top:943px"><div class="get">Get $200</div><div class="in">In Upgrades</div><div class="for">For $140<small>Only</small></div><div class="saving"><b>30%</b><span>Savings</span></div></div>
  <div class="abs upgrade" style="left:1396px;top:943px"><div class="get">Get $400</div><div class="in">In Upgrades</div><div class="for">For $240<small>Only</small></div><div class="saving"><b>40%</b><span>Savings</span></div></div>

  <!-- Flex gift box -->
  <div class="abs offer-box" style="left:1578px;top:887px;width:434px;height:195px"></div>
  <div class="abs tab" style="left:1796px;top:872px">New Flex Members</div>
  <div class="abs box-sub" style="left:1796px;top:907px">Get $135 Sign-Up Gift!</div>
  <div class="abs gift" style="left:1589px;top:943px"><em>$35</em> Lotion Credit</div>
  <div class="abs gift" style="left:1801px;top:943px"><em>$50</em> in Upgrades</div>
  <div class="abs gift" style="left:1589px;top:993px"><em>1 Free</em> Sunless Session</div>
  <div class="abs gift" style="left:1801px;top:993px"><em>1 Free</em> Red Light Session</div>
  <div class="abs gift-note" style="left:1795px;top:1049px">All above gifts valid for 31 days</div>

  <!-- Recommendations -->
  <div class="abs rec-band">SunHaven Recommends</div>

  <div class="abs rec-title" style="left:1105px;top:1227px">Tanning Accelerators<br>(pre-tan)</div>
  <div class="abs rec-copy" style="left:1105px;top:1288px;width:132px">These include the ingredients needed to produce melanin and tan your skin, plus the vitamins and minerals required for proper skin care.&nbsp; Using a good accelerator while give you the same colour in 1-2 sessions, as 2-3 without it, saving you time and money.</div>
  <div class="abs visual" role="img" aria-label="Dark tanning accelerator tube" style="left:1243px;top:1292px;width:35px;height:118px;background:linear-gradient(180deg,#4a4a4a,#111)"></div>
  <div class="abs visual" role="img" aria-label="Silver tanning accelerator tube" style="left:1295px;top:1340px;width:35px;height:118px;background:linear-gradient(180deg,#3a3a3a,#e9e9e9)"></div>

  <div class="abs rec-title" style="left:1471px;top:1227px">Tanning Facial</div>
  <div class="abs rec-copy" style="left:1471px;top:1264px;width:162px">Facial products are specifically formulated for more delicate skin. They are typically loaded with more essential vitamins, minerals and antioxidants that do not clog your pores. They also build beautiful colour, while moisturizing and improving overall skin appearance with each use. It's essential to use a high-quality facial skincare that will protect your skin and glow you've been working on.</div>
  <div class="abs visual" role="img" aria-label="Tanning facial lotion tube" style="left:1660px;top:1296px;width:35px;height:118px;background:linear-gradient(180deg,#2e2e2e,#f0f0f0)"></div>

  <div class="abs rec-title" style="left:1822px;top:1227px">Moisturizer for<br>Tanners (post-tan)</div>
  <div class="abs rec-copy" style="left:1822px;top:1294px;width:108px">Nourish, protect, and extend the life of your tan. Formulated specifically for tanners, this is an important product to replenish &amp; lock in moisture.&nbsp; Use after your tan, and after each shower.</div>
  <div class="abs visual" role="img" aria-label="Green post-tan moisturizer bottle" style="left:1951px;top:1300px;width:52px;height:118px;background:linear-gradient(180deg,#d9ecc8,#a9d08e);border-radius:10px"></div>
</div>
</body>
</html>
```